Business Card For Kelmora Financial Consulting

Hi, I would like a business card designed. Bold, modern.
Please use the same design as the logo. I have also attached the website design to see the overall theme.
Wordmark Font
Color: Hex: #01AEF7

```html
<!DOCTYPE html>
<html lang="en">
<head>
<meta charset="utf-8">
<title>Kelmora Financial Consulting – Business Card</title>
<link href="https://fonts.googleapis.com/css2?family=Montserrat:wght@600&family=Open+Sans:wght@400;600&display=swap" rel="stylesheet">
<style>
  :root {
    --brand-blue: #01AEF7;
    --card-navy: #17212b;
    --card-white: #ffffff;
    --page-bg: #eeeff1;
    --steel-light: #d9dcdf;
    --steel-dark: #8c9095;
    --rule-dim: #2c3844;
  }
  * { box-sizing: border-box; margin: 0; padding: 0; }
  html, body { width: 1200px; height: 800px; overflow: hidden; }
  body {
    background: var(--page-bg);
    font-family: "Open Sans", Arial, sans-serif;
    position: relative;
  }
  .card {
    position: absolute;
    top: 245px;
    width: 520px;
    height: 310px;
    overflow: hidden;
    box-shadow: 0 6px 18px rgba(0,0,0,0.18);
  }
  /* Front */
  .card-front { left: 50px; background: var(--card-navy); }
  .front-rule {
    position: absolute; left: 25%; top: 80px; width: 50%; height: 1px;
    background: var(--rule-dim);
  }
  .wordmark {
    position: absolute; left: 0; right: 0; top: 136px;
    display: flex; justify-content: center; align-items: center; gap: 10px;
  }
  .wordmark-square {
    width: 26px; height: 26px; border: 3px solid var(--brand-blue);
  }
  .wordmark-name {
    font-family: "Montserrat", Arial, sans-serif; font-weight: 600;
    font-size: 17px; letter-spacing: 1.5px; color: var(--card-white);
    text-transform: uppercase;
  }
  .front-baseline {
    position: absolute; left: 28px; top: 284px; width: 410px; height: 5px;
    background: linear-gradient(180deg, var(--steel-light), var(--steel-dark));
  }
  .front-skyline {
    position: absolute; left: 436px; top: 176px; width: 60px; height: 113px;
    background: linear-gradient(135deg, var(--steel-light), var(--steel-dark));
  }
  /* Back */
  .card-back { left: 630px; background: var(--card-white); }
  .name-band {
    position: absolute; left: 38%; right: 0; top: 0; height: 62px;
    background: var(--brand-blue);
    border-bottom-left-radius: 34px;
    display: flex; align-items: center; padding-left: 28px; gap: 14px;
    color: var(--card-white);
  }
  .person-name { font-size: 30px; font-weight: 400; letter-spacing: 0.5px; }
  .person-role { font-size: 10px; margin-top: 6px; }
  .contact-icons {
    position: absolute; left: 142px; top: 108px;
    display: flex; flex-direction: column; gap: 34px;
  }
  .contact-icons svg { width: 18px; height: 18px; display: block; }
  .phone {
    position: absolute; right: 26px; top: 236px;
    display: flex; align-items: center; gap: 6px;
    font-family: "Montserrat", Arial, sans-serif; font-weight: 600;
    font-size: 24px; color: var(--brand-blue);
  }
  .phone svg { width: 16px; height: 16px; }
  .back-baseline {
    position: absolute; left: 128px; top: 280px; width: 372px; height: 5px;
    background: linear-gradient(180deg, var(--steel-light), var(--steel-dark));
  }
  .back-skyline {
    position: absolute; left: 24px; top: 186px; width: 106px; height: 100px;
    background: linear-gradient(135deg, var(--steel-light), var(--steel-dark));
  }
</style>
</head>
<body>
  <section class="card card-front" aria-label="Card front">
    <div class="front-rule"></div>
    <div class="wordmark">
      <span class="wordmark-square"></span>
      <span class="wordmark-name">Kelmora Financial Consulting</span>
    </div>
    <div class="front-baseline"></div>
    <div class="front-skyline" role="img" aria-label="Cut-out city skyline line art"></div>
  </section>

  <section class="card card-back" aria-label="Card back">
    <div class="name-band">
      <span class="person-name">NAME</span>
      <span class="person-role">Consultor Sênior</span>
    </div>
    <div class="contact-icons">
      <svg viewBox="0 0 24 24" aria-label="Email"><path d="M3 10 L12 3 L21 10 V20 H3 Z" fill="var(--brand-blue)"/><path d="M3 10 L12 16 L21 10" fill="none" stroke="#fff" stroke-width="2"/></svg>
      <svg viewBox="0 0 24 24" aria-label="Address"><path d="M12 2 a6 6 0 0 1 6 6 c0 5 -6 11 -6 11 s-6 -6 -6 -11 a6 6 0 0 1 6 -6z" fill="var(--brand-blue)"/><circle cx="12" cy="8" r="2.2" fill="#fff"/><path d="M4 22 H20" stroke="var(--brand-blue)" stroke-width="2"/></svg>
      <svg viewBox="0 0 24 24" aria-label="Website"><circle cx="12" cy="12" r="9" fill="none" stroke="var(--brand-blue)" stroke-width="2.5"/><path d="M3 12 H21 M12 3 C8 8 8 16 12 21 M12 3 C16 8 16 16 12 21" fill="none" stroke="var(--brand-blue)" stroke-width="1.8"/></svg>
    </div>
    <div class="phone">
      <svg viewBox="0 0 24 24" aria-hidden="true"><path d="M6 2 L10 2 L11 7 L8 9 C9 12 12 15 15 16 L17 13 L22 14 L22 18 C22 20 20 22 18 22 C9 21 3 15 2 6 C2 4 4 2 6 2 Z" fill="var(--brand-blue)"/></svg>
      <span>000-000-0000</span>
    </div>
    <div class="back-baseline"></div>
    <div class="back-skyline" role="img" aria-label="Cut-out city skyline line art"></div>
  </section>
</body>
</html>
```